Outgrow the Noise Book Cover

Looking for a cover for my book, Outgrow the Noise. Part memoir, part self help - this book is one woman's journey breaking free of the patriarchy and stepping into her divine purpose. Think "boss ass bitch" in NYC transitions to Spiritual Goddess to the beaches of Costa Rica. We are playing on the archetypes of Wounded Masculine to Divine Feminine. Breaking the mold of being a good girl and owning her wild.

Target Market(s)

25-35 yr old female

Industry/Entity Type

Personal Development, Memoir

Font styles to use
Other font styles liked:
• Pink #ff0099 Yellow #ffdf2b Teal #1fc4cd Outgrow - Brittany The - open sans Noise - Bebas Neue

Colors
FFF300
FFF600
FEFA6F
FFFEC7
FFFEE8
E54698
E96AAD
F1A4CE
F9D9EA
FCEFF6

Requirements
Nice to have

```html
<!DOCTYPE html>
<html lang="en">
<head>
<meta charset="utf-8">
<title>Outgrow the Noise – Book Cover</title>
<link rel="stylesheet" href="https://fonts.googleapis.com/css2?family=Allura&family=Bebas+Neue&family=Open+Sans:ital,wght@1,400&family=Oswald:wght@500&display=swap">
<style>
  :root {
    --page-bg: #ecebe8;
    --pink: #ec1f8f;
    --sun-light: #fbd52c;
    --sun-mid: #f8b52e;
    --sun-deep: #f58a2e;
    --butter: #fff08a;
    --ink: #111111;
  }
  * { margin: 0; padding: 0; box-sizing: border-box; }
  html, body {
    width: 1200px;
    height: 995px;
    overflow: hidden;
    background: var(--page-bg);
  }
  .canvas {
    position: relative;
    width: 1200px;
    height: 995px;
  }
  .cover {
    position: absolute;
    left: 280px;
    top: 18px;
    width: 640px;
    height: 960px;
    overflow: hidden;
    background: linear-gradient(170deg, var(--sun-light) 25%, var(--sun-mid) 60%, var(--sun-deep) 100%);
  }
  .cover-art {
    position: absolute;
    inset: 0;
    width: 100%;
    height: 100%;
  }
  .subtitle {
    position: absolute;
    right: 40px;
    top: 70px;
    width: 360px;
    text-align: right;
    font-family: "Oswald", sans-serif;
    font-weight: 500;
    font-size: 25px;
    line-height: 1.25;
    letter-spacing: 0.5px;
    color: var(--butter);
    text-transform: uppercase;
  }
  .title {
    position: absolute;
    left: 0;
    right: 0;
    top: 380px;
    text-align: center;
    color: var(--ink);
  }
  .title-script {
    display: block;
    font-family: "Allura", cursive;
    font-size: 190px;
    line-height: 1;
    margin-left: 20px;
  }
  .title-joiner {
    display: block;
    font-family: "Open Sans", sans-serif;
    font-style: italic;
    font-size: 38px;
    line-height: 1;
    margin: -20px 0 0 150px;
  }
  .title-main {
    display: block;
    font-family: "Bebas Neue", sans-serif;
    font-size: 250px;
    line-height: 0.9;
    letter-spacing: 6px;
    margin-top: 20px;
  }
</style>
</head>
<body>
<div class="canvas">
  <div class="cover">
    <svg class="cover-art" viewBox="0 0 640 960" xmlns="http://www.w3.org/2000/svg">
      <path class="sky-band" d="M0 0 H640 V268 C520 272 430 300 300 330 C170 305 110 262 0 282 Z" fill="var(--pink)"/>
      <path class="wave-line" d="M0 282 C110 262 170 305 300 330 C430 300 520 272 640 268" fill="none" stroke="var(--ink)" stroke-width="4"/>
      <g role="img" aria-label="Silhouette of a woman with her hair in a bun, rising from the wave">
        <rect x="150" y="130" width="100" height="170" rx="40" fill="var(--sun-light)"/>
      </g>
    </svg>
    <p class="subtitle">Woman's journey breaking free of the patriarchy and stepping into her divine purpose</p>
    <h1 class="title">
      <span class="title-script">Outgrow</span>
      <span class="title-joiner">the</span>
      <span class="title-main">NOISE</span>
    </h1>
  </div>
</div>
</body>
</html>
```